Fashion Label Startup Business Card Design

Maribel Quint is a startup fashion designer based on the Gold Coast in QLD Australia. Maribels label " Vorine by Quint " is based upon taking old world design techniques and infusing them modern twist. The card design should incorporate an old world theme using colours like mustard, ocha, black, white and elements of lace pattern.

Card Details:

Maribel Quint
Fashion Designer
P: 04 0152 6847
E: vorinebyquint@mailbrook.com
W: www.friendsnet.com/VOrineByQuint

```html
<!DOCTYPE html>
<html lang="en">
<head>
<meta charset="utf-8">
<title>Maribel Quint – Business Card</title>
<link href="https://fonts.googleapis.com/css2?family=Poiret+One&display=swap" rel="stylesheet">
<style>
  :root {
    --teal-deep: #2c6479;
    --teal-mid: #3f7585;
    --lace-tone: #6f8f92;
    --lace-light: #8fa6a2;
    --ring-cream: #c6c8b7;
    --disc-centre: #8fb2b4;
    --disc-edge: #3c7083;
    --text-white: #ffffff;
  }
  html, body {
    margin: 0;
    padding: 0;
    overflow: hidden;
    background: var(--teal-deep);
  }
  .card {
    position: relative;
    width: 1200px;
    height: 667px;
    overflow: hidden;
    background: var(--teal-deep);
    font-family: "Poiret One", sans-serif;
    color: var(--text-white);
  }
  .card__art {
    position: absolute;
    inset: 0;
  }
  .card__name {
    position: absolute;
    right: 438px;
    top: 204px;
    margin: 0;
    font-size: 52px;
    font-weight: 400;
    letter-spacing: 0.5px;
    line-height: 1;
  }
  .card__role {
    position: absolute;
    right: 432px;
    top: 266px;
    margin: 0;
    font-size: 23px;
    font-weight: 400;
    line-height: 1;
  }
  .card__contact {
    position: absolute;
    left: 0;
    width: 1192px;
    top: 357px;
    margin: 0;
    padding: 0;
    list-style: none;
    text-align: center;
    font-size: 20px;
    font-weight: 700;
    line-height: 30.5px;
  }
</style>
</head>
<body>
  <div class="card">
    <svg class="card__art" width="1200" height="667" viewBox="0 0 1200 667">
      <defs>
        <radialGradient id="disc-glow" cx="0.5" cy="0.5" r="0.5">
          <stop offset="0" stop-color="var(--disc-centre)"/>
          <stop offset="1" stop-color="var(--disc-edge)"/>
        </radialGradient>
        <radialGradient id="lace-wash" cx="0.5" cy="0.5" r="0.5">
          <stop offset="0.65" stop-color="var(--lace-light)"/>
          <stop offset="1" stop-color="var(--lace-tone)"/>
        </radialGradient>
      </defs>
      <circle class="lace-wreath" cx="598" cy="333" r="335" fill="url(#lace-wash)" opacity="0.55"
              role="img" aria-label="Cream lace ornament wreath surrounding the central disc"/>
      <circle class="centre-disc" cx="598" cy="333" r="231" fill="url(#disc-glow)"
              stroke="var(--ring-cream)" stroke-width="6"/>
    </svg>

    <h1 class="card__name">Maribel Quint</h1>
    <p class="card__role">Fashion Designer</p>

    <ul class="card__contact">
      <li>Tél: 04 0152 6847</li>
      <li>E-mail: vorinebyquint@mailbrook.com</li>
      <li>Website: www.friendsnet.com/VOrineByQuint</li>
    </ul>
  </div>
</body>
</html>
```